Business Card Design

We need a business card that reflects a company that has been established for over 20 years, a card that displays confidence.
Although we are established we are forward thinking and always pushing forward.
Our company buys, processes and exports scrap metal all over the world.
We buy metal from all around Australia, although we sell it all across the globe.
The card should look modern, bold, but not over complicated.
Incorporate the Logo and the company colors.
Would like to see in raised lettering.
Updates

Thank you to all designers, same amazing designs in such a short time.

At this stage designer Porvil is the front runner.
The design is crisp, clean and modern, not to busy.
I would like to see what you all come up with in the next 24 hours.
Thank you

Industry/Entity Type

Business

Contact Information for Business Card

Dunmore Metal Recyclers
Greg Pavlenko
Director
3-7 Wandle Road
Burton, South Australia 5110
Phone +61-8-8357-4120
Fax +61-8-8357 1934
Mobile 0429 513 806
email: greg@dunmoremr.example
web: www.dunmoremr.example

```html
<!DOCTYPE html>
<html lang="en">
<head>
<meta charset="utf-8">
<title>Dunmore Metal Recyclers – Business Card</title>
<link rel="stylesheet" href="https://fonts.googleapis.com/css2?family=Fira+Sans+Extra+Condensed:ital,wght@0,400;0,600;0,700;1,500&display=swap">
<style>
  :root {
    --ink-black: #000000;
    --paper: #ffffff;
    --brand-green: #3e7a33;
    --soft-green: #7ea86c;
    --text-grey: #3b3b3b;
    --logo-white: #ffffff;
  }
  html, body {
    margin: 0;
    padding: 0;
    width: 1200px;
    height: 741px;
    overflow: hidden;
    background: var(--paper);
  }
  .card {
    position: relative;
    width: 1200px;
    height: 741px;
    background: var(--paper);
    font-family: "Fira Sans Extra Condensed", "Arial Narrow", sans-serif;
    overflow: hidden;
  }
  .brand-panel {
    position: absolute;
    left: 0;
    top: 0;
    width: 296px;
    height: 741px;
    background: var(--ink-black);
  }
  .panel-pointer {
    position: absolute;
    left: 295px;
    top: 327px;
  }
  .brand-mark {
    position: absolute;
    left: 0;
    top: 300px;
    width: 296px;
    text-align: center;
    color: var(--logo-white);
    font-weight: 600;
  }
  .brand-mark .dot {
    display: block;
    width: 58px;
    height: 58px;
    margin: 0 auto 14px;
    border-radius: 50%;
    background: var(--soft-green);
  }
  .brand-mark .brand-name {
    font-size: 34px;
    line-height: 1.05;
    letter-spacing: 0.5px;
  }
  .identity {
    position: absolute;
    right: 44px;
    top: 344px;
    text-align: right;
  }
  .person-name {
    margin: 0;
    font-size: 58px;
    font-weight: 700;
    line-height: 1;
    color: var(--brand-green);
    letter-spacing: 0.3px;
  }
  .person-role {
    margin: 2px 0 0;
    font-size: 44px;
    font-style: italic;
    font-weight: 500;
    line-height: 1;
    color: var(--soft-green);
  }
  .contact {
    position: absolute;
    right: 44px;
    top: 534px;
    margin: 0;
    text-align: right;
    color: var(--text-grey);
    font-size: 34px;
    font-weight: 400;
    line-height: 49px;
  }
  .contact p { margin: 0; white-space: nowrap; }
  .contact .label { font-weight: 600; }
</style>
</head>
<body>
  <main class="card">
    <div class="brand-panel"></div>
    <svg class="panel-pointer" width="40" height="88" viewBox="0 0 40 88" aria-hidden="true">
      <polygon points="0,0 38,44 0,88" fill="var(--ink-black)"/>
    </svg>

    <div class="brand-mark">
      <span class="dot"></span>
      <div class="brand-name">Dunmore<br>Metal Recyclers</div>
    </div>

    <header class="identity">
      <h1 class="person-name">GREG PAVLENKO</h1>
      <p class="person-role">Director</p>
    </header>

    <address class="contact">
      <p>3-7 Wandle Road Burton, South Australia - 5110</p>
      <p><span class="label">P:</span> +61.8.8357.4120 | <span class="label">F:</span> +61.8.8357.1934 | <span class="label">M:</span> 0429.513.806</p>
      <p><span class="label">E:</span> greg@dunmoremr.example&nbsp; | <span class="label">W:</span> dunmoremr.example</p>
    </address>
  </main>
</body>
</html>
```